Creative Frame Mat for 40Forge Challenge

I am gifting a present to my wife and am looking for your help to make it happen. I have a 8"x10" picture frame. In it, I want to place a 4"x6" picture. The rest of that space is the creative area I am looking for your help. Let's call it a picture border or mat. I don't care where the 4"x6" cut out for the picture is. You get to decide. The border or mat is to have a #40Forge theme. Images are below. You can incorporate some/all or add your own design.

Target Market(s)

Gym / health / self help enthusiast

Font styles to use
Sans Serif
Decorative

Requirements
Must have
• - Frame mat is 8" x 10"
- Include a cut out area for a picture to be inserted that is 4" x 6"
- A main header with "40FORGE"
Nice to have
• Color: Black, grey, white and red
Optional quotes to add in small text:
- I can do more
- Discipline
- Determination
- Perseverance
- Grit
- Confidence
- Self-Belief
- Self-Esteem
- Self-Worth

```html
<!DOCTYPE html>
<html lang="en">
<head>
<meta charset="UTF-8">
<title>40Forge Frame Mat</title>
<link rel="stylesheet" href="https://fonts.googleapis.com/css2?family=Arimo:wght@400&display=swap">
<style>
  :root {
    --mat-red: #c41f25;
    --ink-black: #000000;
    --paper-white: #ffffff;
    --edge-dark: #2a2a2a;
  }
  * { margin: 0; padding: 0; box-sizing: border-box; }
  html, body { width: 960px; height: 1200px; overflow: hidden; background: var(--mat-red); }
  .mat {
    position: relative;
    width: 960px;
    height: 1200px;
    background: var(--mat-red);
    border: 1px solid var(--edge-dark);
    font-family: "Arimo", Arial, sans-serif;
    overflow: hidden;
  }
  .header-panel {
    position: absolute;
    left: 94px; top: 0;
    width: 772px; height: 744px;
    background: var(--ink-black);
  }
  .headline {
    position: absolute;
    left: 0; top: 130px;
    width: 960px;
    text-align: center;
    padding-left: 6px;
    font-size: 46px;
    line-height: 1;
    letter-spacing: 7px;
    color: var(--mat-red);
    font-weight: 400;
  }
  .headline-underline {
    position: absolute;
    left: 536px; top: 183px;
    width: 161px; height: 2px;
    background: var(--paper-white);
  }
  .photo-opening {
    position: absolute;
    left: 120px; top: 240px;
    width: 719px; height: 479px;
    background: var(--paper-white);
  }
  .values-band {
    position: absolute;
    left: 0; top: 835px;
    width: 960px; height: 302px;
    background: var(--ink-black);
  }
  .value-rule {
    position: absolute;
    height: 3px;
    background: var(--mat-red);
  }
  .value-rule.left { left: 0; width: 335px; }
  .value-rule.right { left: 625px; width: 335px; }
  .value {
    position: absolute;
    font-size: 23px;
    line-height: 1;
    letter-spacing: 3px;
    color: var(--paper-white);
    white-space: nowrap;
  }
  .value.left { left: 93px; }
  .value.right { right: 93px; text-align: right; margin-right: -3px; }
  .brand-mark {
    position: absolute;
    left: 387px; top: 850px;
    width: 200px; height: 270px;
  }
  .brand-dot {
    position: absolute;
    left: 50px; top: 20px;
    width: 100px; height: 100px;
    border-radius: 50%;
    border: 4px solid var(--mat-red);
  }
  .brand-name {
    position: absolute;
    left: 0; top: 185px;
    width: 200px;
    text-align: center;
    font-size: 34px;
    line-height: 1;
    letter-spacing: 2px;
    color: var(--paper-white);
  }
</style>
</head>
<body>
  <div class="mat">
    <div class="header-panel"></div>
    <h1 class="headline">I CAN DO MORE</h1>
    <div class="headline-underline"></div>
    <div class="photo-opening" aria-label="4 by 6 inch photo opening"></div>

    <div class="values-band"></div>

    <div class="value-rule left" style="top:917px"></div>
    <div class="value-rule left" style="top:977px"></div>
    <div class="value-rule left" style="top:1041px"></div>
    <div class="value-rule right" style="top:917px"></div>
    <div class="value-rule right" style="top:977px"></div>
    <div class="value-rule right" style="top:1041px"></div>

    <div class="value left" style="top:879px">DISCIPLINE</div>
    <div class="value left" style="top:942px">DETERMINATION</div>
    <div class="value left" style="top:1005px">PERSEVERANCE</div>
    <div class="value left" style="top:1067px">GRIT</div>

    <div class="value right" style="top:879px">CONFIDENCE</div>
    <div class="value right" style="top:942px">SELF-BELIEF</div>
    <div class="value right" style="top:1005px">SELF-ESTEEM</div>
    <div class="value right" style="top:1067px">SELF-WORTH</div>

    <div class="brand-mark">
      <div class="brand-dot"></div>
      <div class="brand-name">40FORGE</div>
    </div>
  </div>
</body>
</html>
```